Bold Website Design for Fitness Trainer - No Coding

We are in need of a bold and unique website design for a personal fitness training company, www.TessaRowle.com. We need DESIGN ONLY for three pages. These will be a homepage, a lead capture page, and one internal page with a sidebar. The design will be used for coding a wordpress theme, if that matters for the designer.

Tessa Rowle Fitness Training
2718 E 57th St #193
Austin, TX 78705
512-460-7198
http://www.tessarowle.com

Target Market(s)

18-45 year old male and females making 80k+ a year and looking to get stronger and in shape.

Industry/Entity Type

Fitness

Number of Pages Required

3 page

Font styles to use
Sans Serif

Requirements
Must have
• See attached design specs file.
Nice to have
Should not have
• Boxed layout.
• Dark Background.

```html
<!DOCTYPE html>
<html lang="en">
<head>
<meta charset="utf-8">
<title>TessaRowle Real Fitness Training</title>
<link href="https://fonts.googleapis.com/css2?family=Montserrat:wght@400;600;700;800&family=Open+Sans:ital,wght@0,400;0,700;1,700&display=swap" rel="stylesheet">
<style>
:root{
  --black:#121212;
  --charcoal:#1f1f1f;
  --grey-btn:#3a3a3a;
  --orange-a:#ff5a00;
  --orange-b:#ffa914;
  --yellow:#ffe81a;
  --red:#ee3b47;
  --cyan:#1ec8f0;
  --light:#efefef;
  --white:#ffffff;
  --text:#151515;
  --muted:#777777;
  --foot-bar:#cfcfcf;
}
*{margin:0;padding:0;box-sizing:border-box}
html,body{width:1200px;height:3428px;overflow:hidden;background:var(--white)}
body{font-family:'Open Sans',sans-serif;color:var(--text);position:relative}
.abs{position:absolute}
.display{font-family:'Montserrat',sans-serif;font-weight:800;text-transform:uppercase}

/* top bar */
.topbar{top:0;left:0;width:1200px;height:56px;background:var(--black);color:var(--white);font-family:'Montserrat',sans-serif;font-size:14px;font-weight:600;display:flex;align-items:center;padding:0 70px;gap:56px}
.topbar .item{display:flex;align-items:center;gap:10px}
.social{display:flex;gap:14px;margin-left:auto}
.social span{width:16px;height:16px;border-radius:50%;background:var(--white);display:block}

/* nav */
.nav{top:56px;left:0;width:1200px;height:72px;background:var(--black);display:flex;align-items:center;padding-left:70px;gap:40px;font-family:'Montserrat',sans-serif;font-weight:700;font-size:15px;color:var(--white)}
.nav .free{position:absolute;right:0;top:0;height:72px;width:168px;background:var(--grey-btn);display:flex;align-items:center;justify-content:center}

/* hero */
.hero{top:128px;left:0;width:1200px;height:532px;background:linear-gradient(100deg,var(--orange-a) 0%,#ff7a00 45%,var(--orange-b) 100%)}
.hero-photo{top:0;left:300px;width:360px;height:300px;background:radial-gradient(ellipse at 50% 40%,rgba(255,225,200,.45),rgba(255,120,0,0) 70%)}
.hero-title{top:112px;left:0;width:1200px;text-align:center;color:var(--white);font-size:50px;line-height:54px}
.hero-sub{top:244px;left:0;width:1200px;text-align:center;color:var(--white);font-size:15px;line-height:22px}
.btn{background:var(--yellow);color:var(--text);font-family:'Montserrat',sans-serif;font-weight:700;font-size:15px;display:flex;align-items:center;justify-content:center;text-transform:uppercase}
.hero .btn{top:420px;left:510px;width:180px;height:52px}

/* intro */
.intro{top:720px;left:0;width:1200px;text-align:center;font-size:23px;line-height:32px;font-weight:700}
.intro p+p{margin-top:28px}

/* services */
.tile{display:flex;align-items:center;justify-content:center;text-align:center;color:var(--white);font-size:40px;line-height:44px;text-shadow:none}
.tile-personal{top:1000px;left:0;width:596px;height:512px;background:linear-gradient(120deg,#9a9ea4,#5e646b 55%,#30353b)}
.tile-strength{top:1000px;left:604px;width:596px;height:248px;background:linear-gradient(120deg,#3c4450,#7a8696 60%,#b5bcc5)}
.tile-online{top:1256px;left:604px;width:596px;height:256px;background:linear-gradient(120deg,#c6c9cc,#8f959b 60%,#5c6167)}

/* testimonial */
.testimonial{top:1580px;left:0;width:1200px;height:360px;background:var(--light)}
.testi-photo{top:0;left:860px;width:340px;height:360px;background:linear-gradient(90deg,#e8e8e8,#cfc7c0 60%,#b9aea4)}
.arrow{top:80px;left:590px}
.quote{top:200px;left:140px;width:440px;font-size:21px;line-height:28px;font-weight:700;font-style:italic}
.cite{top:318px;left:400px;width:180px;text-align:right;font-size:12px;line-height:16px;color:var(--muted)}

/* blog */
.blog-photo{top:2000px;left:0;width:400px;height:620px;background:linear-gradient(110deg,#7a3a22,#c4663d 50%,#e59a6a)}
.blog-panel{top:2000px;left:250px;width:950px;height:620px;background:var(--red);clip-path:polygon(40px 0,100% 0,100% 100%,0 100%)}
.blog-label{top:96px;left:90px;color:var(--white);font-size:32px}
.dots{top:110px;left:780px;display:flex;gap:10px}
.dots span{width:10px;height:10px;border-radius:50%;background:#f6a3a9}
.dots span:first-child{background:var(--white)}
.blog-title{top:196px;left:90px;color:var(--white);font-family:'Montserrat',sans-serif;font-weight:700;font-size:36px}
.blog-text{top:262px;left:90px;width:740px;color:var(--white);font-size:15px;line-height:22px}
.blog-panel .btn{top:468px;left:90px;width:160px;height:52px}

/* cta */
.cta{top:2688px;left:0;width:1200px;height:212px;background:var(--charcoal)}
.cta-text{top:58px;left:140px;color:var(--white);font-size:38px;line-height:46px}
.cta .btn{top:80px;left:830px;width:180px;height:52px}

/* footer */
.foot-brand{top:2990px;left:60px;font-size:30px}
.foot-about{top:3070px;left:60px;width:420px;font-size:17px;line-height:25px;color:#333}
.foot-address{top:3226px;left:60px;display:flex;gap:18px;font-size:16px;line-height:22px;color:#333}
.foot-links{top:2980px;left:584px;font-size:26px;line-height:34px;font-family:'Montserrat',sans-serif;font-weight:800;text-transform:uppercase;list-style:none}
.foot-social{top:3240px;left:584px;display:flex;gap:16px}
.foot-social span{width:18px;height:18px;border-radius:50%;background:var(--text);display:block}
.copyright{top:3380px;left:0;width:1200px;height:48px;background:var(--foot-bar);display:flex;align-items:center;justify-content:center;font-family:'Montserrat',sans-serif;font-weight:700;font-size:13px;color:#333}
</style>
</head>
<body>

<header>
  <div class="abs topbar">
    <div class="item">
      <svg width="14" height="14" viewBox="0 0 24 24"><path d="M6.6 10.8a15 15 0 006.6 6.6l2.2-2.2a1 1 0 011-.25 11.4 11.4 0 003.6.57 1 1 0 011 1V20a1 1 0 01-1 1A17 17 0 013 4a1 1 0 011-1h3.5a1 1 0 011 1 11.4 11.4 0 00.57 3.6 1 1 0 01-.25 1z" fill="#fff"/></svg>
      (132) 555 0148
    </div>
    <div class="item">
      <svg width="16" height="12" viewBox="0 0 16 12"><rect x="0.5" y="0.5" width="15" height="11" fill="none" stroke="#fff"/><path d="M1 1l7 6 7-6" fill="none" stroke="#fff"/></svg>
      INFO@TESSAROWLE.COM
    </div>
    <div class="item">
      <svg width="14" height="14" viewBox="0 0 14 14"><rect x="0.5" y="2" width="13" height="11.5" fill="none" stroke="#fff"/><path d="M0.5 5.5h13M4 0v3M10 0v3" stroke="#fff"/></svg>
      OUR APPOINTMENT CALENDAR
    </div>
    <div class="social"><span></span><span></span><span></span><span></span></div>
  </div>
  <nav class="abs nav">
    <span>HOME</span><span>PROGRAMS</span><span>MEET YOUR TRAINER</span><span>BLOG</span><span>CONTACT</span>
    <span class="free">FREE SESSION</span>
  </nav>
</header>

<section class="abs hero">
  <div class="abs hero-photo" role="img" aria-label="Photo of a woman stretching in an athletic pose"></div>
  <h1 class="abs hero-title display">TessaRowle™<br>Real Fitness Training</h1>
  <p class="abs hero-sub">Feel the difference of being fit. Subscribe your free training session<br>and discover the programs we have for you.</p>
  <a class="abs btn">Get Started</a>
</section>

<section class="abs intro">
  <p>CHANGE IS HARD. GETTING FIT IS HARDER.<br>YOU MIGHT THINK YOU'LL NEVER BE ABLE TO GET IN SHAPE BECAUSE<br>THERE'S A LOT YOU HAVE TO DO ON YOUR OWN .</p>
  <p>OUR TRAINERS WILL TAKE YOU THROUGHOUT A JOURNEY TO<br>EXPERIENCE THE DIFFERENCE OF BEING FIT, HAPPY AND HEALTHY.</p>
</section>

<section>
  <div class="abs tile tile-personal display" role="img" aria-label="Photo of a man lifting dumbbells on a bench">1-on-1<br>Personal<br>Training</div>
  <div class="abs tile tile-strength display" role="img" aria-label="Photo of a man training with weights">Strength<br>Programming</div>
  <div class="abs tile tile-online display" role="img" aria-label="Photo of a person following an online workout">Online<br>Coaching</div>
</section>

<section class="abs testimonial">
  <div class="abs testi-photo" role="img" aria-label="Photo of a smiling woman in a sports top"></div>
  <svg class="abs arrow" width="22" height="40" viewBox="0 0 22 40"><path d="M3 3l15 17-15 17" fill="none" stroke="var(--cyan)" stroke-width="6"/></svg>
  <blockquote class="abs quote">"My to-do list is very large and I couldn't but write off my workout time. I contacted Tessa to start a personal training. Since then I fend off weight and boost my productivity. "</blockquote>
  <p class="abs cite">CLARA<br>Account manager</p>
</section>

<section>
  <div class="abs blog-photo" role="img" aria-label="Photo of a muscular arm during a workout"></div>
  <div class="abs blog-panel">
    <h2 class="abs blog-label display">From the Blog</h2>
    <div class="abs dots"><span></span><span></span><span></span></div>
    <h3 class="abs blog-title">The science behind the madness</h3>
    <p class="abs blog-text">If you want to lose weight fast, think again. Just like getting rich, it doesn't happen overnight. There are many plans that tell you that if you do different things you will achieve a specific result. One of the questions nutritionists and weight loss experts often get asked is: "How much weight will you lose if you work out an hour a day?"</p>
    <a class="abs btn">Read More</a>
  </div>
</section>

<section class="abs cta">
  <h2 class="abs cta-text display">Start your training today.<br>Your first sesion is on us.</h2>
  <a class="abs btn">Get Started</a>
</section>

<footer>
  <h2 class="abs foot-brand display">TessaRowle™</h2>
  <p class="abs foot-about">Headquartered in Sydney, TessaRowle is a health club industry pioneer, serving nearly four thousands members in more than 20 clubs across Australia.</p>
  <div class="abs foot-address">
    <svg width="14" height="20" viewBox="0 0 14 20"><path d="M7 0a7 7 0 00-7 7c0 5 7 13 7 13s7-8 7-13a7 7 0 00-7-7zm0 10a3 3 0 110-6 3 3 0 010 6z" fill="#333"/></svg>
    <span>48, Harbour Lane, Sydney 12092<br>Australia</span>
  </div>
  <ul class="abs foot-links"><li>Home</li><li>Programs</li><li>Meet Your Trainer</li><li>Blog</li><li>Contact</li></ul>
  <div class="abs foot-social"><span></span><span></span><span></span><span></span></div>
  <div class="abs copyright">©2015 TESSAROWLE INC. ALL RIGHTS RESERVED.</div>
</footer>

</body>
</html>
```